"Breathe & Bloom" Book Cover 5.5x8.5

Title of the book is "Breathe & Bloom"
Subtitle is "Unmasking Pricing Myths"
I've used PixelGuild on multiple occasions you can look on my Borvex page, Mark Delwitt, to see the covers I've used in the other projects I've done.
The target audience are people who have been tricked to think they can't retire because inflation, i.e. cost of living is going up so much they must work to keep up. There is no evidence of this.
And those are the people I want to reach so they can "Breathe...and Bloom."
Target Market(s)
Americans aged 55 and over who are thinking about retirement
Industry/Entity Type
Financial
Requirements
Nice to have
- Keep It Simple, Stupid is my mantra. Just make it pop out when people are browsing
Should not have
- No piggy banks. No old people sitting on a beach.

```html
<!DOCTYPE html>
<html lang="en">
<head>
<meta charset="utf-8">
<title>Breathe &amp; Bloom — Book Cover</title>
<link rel="stylesheet" href="https://fonts.googleapis.com/css2?family=EB+Garamond:wght@400&display=swap">
<style>
  :root {
    --paper: #ffffff;
    --ink: #111111;
    --accent-red: #e3141c;
    --sky-light: #fbfcfa;
    --sky-haze: #eef0e6;
    --grass-light: #b6ad6a;
    --grass-deep: #857a3c;
  }
  html, body {
    margin: 0;
    padding: 0;
    width: 776px;
    height: 1200px;
    overflow: hidden;
    background: var(--paper);
  }
  .cover {
    position: relative;
    width: 776px;
    height: 1200px;
    background: var(--paper);
    overflow: hidden;
    font-family: "EB Garamond", Georgia, serif;
  }
  .cover-photo {
    position: absolute;
    left: 0;
    top: 760px;
    width: 776px;
    height: 440px;
    background: linear-gradient(to bottom,
      var(--paper) 0%,
      var(--sky-light) 30%,
      var(--sky-haze) 50%,
      var(--grass-light) 56%,
      var(--grass-light) 70%,
      var(--grass-deep) 100%);
  }
  .cover-type {
    position: absolute;
    inset: 0;
  }
  .title-word { fill: var(--ink); font-family: "EB Garamond", Georgia, serif; }
  .title-amp { fill: var(--ink); font-family: "EB Garamond", Georgia, serif; }
  .subtitle { fill: var(--accent-red); font-family: "EB Garamond", Georgia, serif; }
  .author { fill: var(--ink); font-family: "EB Garamond", Georgia, serif; }
</style>
</head>
<body>
  <main class="cover">
    <div class="cover-photo" role="img" aria-label="Photo of a retired couple walking away across a sunlit grassy field, pushing a yellow bicycle with a wicker basket"></div>

    <svg class="cover-type" width="776" height="1200" viewBox="0 0 776 1200" aria-labelledby="book-title">
      <title id="book-title">Breathe &amp; Bloom: Unmasking Pricing Myths by Mark Delwitt</title>
      <text class="title-word" x="66" y="318" font-size="200" textLength="562" lengthAdjust="spacingAndGlyphs">Breathe</text>
      <text class="title-amp" x="634" y="376" font-size="104">&amp;</text>
      <text class="title-word" x="66" y="498" font-size="200" textLength="600" lengthAdjust="spacingAndGlyphs">Bloom</text>
      <text class="subtitle" x="70" y="574" font-size="52" textLength="594" lengthAdjust="spacingAndGlyphs">Unmasking Pricing Myths</text>
      <text class="author" x="758" y="988" font-size="44" text-anchor="end">Mark Delwitt</text>
    </svg>
  </main>
</body>
</html>
```